New Web Page Design - Cement Rendering Business

Looking for a overhaul of our existing website (www.veltro-render.com.au).

Looking for a sleek and elegant design that incorporates the colours of our logos, black / green and white. Needs to look professional and want it to be well above what our competition is offering. (Findora search for 'cement rendering sydney' will display the competition we want to be well ahead of.

Prefer a mixture of pages with black background and white alternatively between home (black), about us (white), contact us (black) and gallery (white).

Would like to incorporate our logo on all pages attached preferably in the top left corner.

Website needs to be search engine optimised and have easily updated photo gallery which we already have.

Also need to embed our trackwise metrics code on the front home page.

Website needs to be able easily updated (text, pictures ) as required.
content management system should include fields where you can alter your page titles, meta description and keywords.

Pages also needs to be optimised for mobile devices, iphone, ipad and other mobile devices. (it is a current feature we have)

If you have any questions, just message me.

Please remember the look and feel of the site is important to us, we don't want it over complicated, simple elegant and professional in line with our logo standards.
Updates

Hi All, As an example of the look and feel we like. We have found a site that may assist in your design and creative process. http://demo.quorvix.org/ We like the simplicity, elegance and professional look of this site, although we would like it with our images, colours and logos. I hope this helps.! keep the great designs coming!

All, Thanks for the designs. Please try and use our website images due to copyright reasons for all your designs. Tomas

Target Market(s)

Construction Companies

Industry/Entity Type

Business

Colors
9bcb3b
acd036
474747

Requirements
Must have
• Search Engine Optimised.
Photo Gallery
Elegant/Professional Look & Feel.
Simple Yet Effective
Nice to have
• Moving Parts
Should not have
• Overly Complicated.
Cheap & Traditional Looking.
Boring

```html
<!DOCTYPE html>
<html lang="en">
<head>
<meta charset="utf-8">
<title>Veltro Cement Rendering</title>
<link href="https://fonts.googleapis.com/css2?family=Quicksand:wght@400;500;700&family=Open+Sans:wght@400;600;700&display=swap" rel="stylesheet">
<style>
:root{
  --green:#9bcb3b;
  --green-bright:#acd036;
  --grey:#474747;
  --charcoal:#3a3a3a;
  --dark:#2a2a2a;
  --header:#1d1d1d;
  --footer:#232323;
  --ink:#111;
  --white:#ffffff;
  --muted:#cfcfcf;
}
*{margin:0;padding:0;box-sizing:border-box}
html,body{width:778px;height:1200px;overflow:hidden;background:var(--dark)}
body{font-family:"Open Sans",Arial,sans-serif;color:var(--white)}
.page{position:relative;width:778px;height:1200px;overflow:hidden;background:var(--grey)}

/* header */
.site-header{position:absolute;left:0;top:0;width:778px;height:62px;background:var(--header);display:flex;align-items:center;justify-content:space-between;padding:0 40px 0 40px}
.brand{display:flex;align-items:center;gap:8px;font-family:"Quicksand",sans-serif;font-weight:700;font-size:18px;color:var(--green);letter-spacing:1px}
.brand-dot{width:22px;height:22px;border-radius:50%;background:var(--green)}
.main-nav{display:flex;align-items:center;gap:16px;font-size:8px;font-weight:600;letter-spacing:.5px}
.main-nav a{color:var(--white);text-decoration:none}
.main-nav .book{background:var(--green);padding:5px 8px;color:var(--white)}

/* hero */
.hero{position:absolute;left:0;top:62px;width:778px;height:330px;background:radial-gradient(ellipse at 50% 40%,#4a4a4a,#303030)}
.slider{position:absolute;left:104px;top:20px;width:572px;height:262px;background:var(--ink);padding:10px;box-shadow:0 6px 18px rgba(0,0,0,.6)}
.slide-photo{position:relative;width:100%;height:100%;background:linear-gradient(100deg,#8a8a8a 0%,#c9c9c9 35%,#e8e8e6 60%,#b9b9b6 100%)}
.slide-caption{position:absolute;left:22px;bottom:44px}
.slide-caption h2{font-family:"Quicksand",sans-serif;font-weight:500;font-size:20px;color:var(--white)}
.slide-caption p{font-size:8px;color:var(--white);margin-top:3px}
.slide-dots{position:absolute;left:50%;bottom:12px;transform:translateX(-50%);display:flex;gap:6px}
.slide-dots span{width:7px;height:7px;border-radius:50%;background:rgba(255,255,255,.55)}
.slide-dots span.active{background:var(--white)}
.tag{position:absolute;background:var(--white);color:#333;font-size:7px;font-weight:600;padding:5px 9px;border:1px solid #999;box-shadow:0 2px 4px rgba(0,0,0,.5)}
.tag-left{left:16px;top:240px;transform:rotate(-35deg)}
.tag-right{left:700px;top:220px;transform:rotate(40deg)}

/* welcome */
.welcome{position:absolute;left:0;top:392px;width:778px;height:200px;background:var(--charcoal);text-align:center;padding:10px 104px 0}
.welcome h1{font-family:"Quicksand",sans-serif;font-weight:700;font-size:12px;color:var(--green);letter-spacing:.5px}
.welcome p{font-size:8.4px;line-height:1.55;color:var(--muted);margin-top:14px}
.welcome .callout{font-family:"Quicksand",sans-serif;font-weight:500;font-size:20px;color:var(--green);margin-top:12px}

/* green band */
.green-band{position:absolute;left:0;top:575px;width:778px;height:420px}
.cta{position:absolute;left:301px;top:600px;width:176px;height:36px;border:2px solid var(--ink);background:var(--dark);color:var(--white);font-weight:700;font-size:11px;letter-spacing:.5px;display:flex;align-items:center;justify-content:center}
.gallery-title{position:absolute;left:0;top:722px;width:778px;text-align:center;font-weight:700;font-size:11px;color:var(--white)}

/* gallery */
.gallery-side{position:absolute;top:772px;width:100px;height:170px;background:linear-gradient(180deg,#c8c8c4,#8f8f8b);border:4px solid var(--white)}
.gallery-left{left:150px}
.gallery-right{left:528px;background:linear-gradient(180deg,#b7b2a8,#7f7a70)}
.gallery-main{position:absolute;left:232px;top:748px;width:306px;height:214px;background:linear-gradient(160deg,#e4e4e2,#a9a9a6);border:5px solid var(--white);box-shadow:0 6px 14px rgba(0,0,0,.5)}
.arrow{position:absolute;top:846px;width:20px;height:20px;border-radius:50%;background:var(--white)}
.arrow-prev{left:222px}
.arrow-next{left:528px}

/* footer */
.site-footer{position:absolute;left:0;top:995px;width:778px;height:205px;background:var(--footer)}
.footer-col{position:absolute;top:22px;font-size:7px;line-height:1.75;color:var(--muted)}
.footer-col h3{font-size:7.5px;font-weight:700;color:var(--white);margin-bottom:10px;letter-spacing:.4px}
.col-links{left:104px}
.col-contact{left:214px;width:130px}
.col-location{left:350px}
.col-social{left:575px;width:100px}
.map{width:180px;height:70px;background:linear-gradient(135deg,#d9e1cf,#b9c7d6)}
.social{display:flex;justify-content:space-between;align-items:center;margin-bottom:6px}
.social i{width:12px;height:12px;border-radius:50%;background:var(--green)}
.copyright{position:absolute;left:0;bottom:0;width:778px;height:28px;background:#181818;display:flex;align-items:center;justify-content:center;font-size:7px;color:var(--muted);letter-spacing:.4px}
</style>
</head>
<body>
<div class="page">

  <header class="site-header">
    <div class="brand"><span class="brand-dot"></span>VELTRO</div>
    <nav class="main-nav">
      <a href="#">HOME</a><a href="#">ABOUT US</a><a href="#">PHOTO GALLERY</a><a href="#">CONTACT US</a><a class="book" href="#">BOOK NOW</a>
    </nav>
  </header>

  <section class="hero">
    <div class="slider">
      <div class="slide-photo" role="img" aria-label="Plasterer applying cement render with a trowel">
        <div class="slide-caption">
          <h2>Welcome to Veltro,</h2>
          <p>your one stop shop for all your cement rendering needs.</p>
        </div>
        <div class="slide-dots"><span class="active"></span><span></span><span></span><span></span></div>
      </div>
    </div>
    <div class="tag tag-left">Quality Finish</div>
    <div class="tag tag-right">Free Quotes</div>
  </section>

  <section class="welcome">
    <h1>WELCOME TO VELTRO CEMENT REDERING</h1>
    <p>Your one stop shop for all your cement rendering needs. We are an Australian owned and operated business with over 25 years of experience in our field. Our work is fully licensed, our employees are trained to the highest standards and all of our work is covered by warranty. We offer an obligation free on-site consultation and quotation service for your convenience 7 days per week. We are the preferred supplier for many of the top building companies in Australia which gives you access to our expertise, competitive rates and peace of mind.</p>
    <p>No job is too big or too small. We work on several residential, private and commercial projects all year round.</p>
    <div class="callout">Give us a call! Obligation free!</div>
  </section>

  <svg class="green-band" viewBox="0 0 778 420" width="778" height="420" aria-hidden="true">
    <polygon fill="#9bcb3b" points="0,14 30,6 52,16 80,4 110,12 140,2 170,14 205,6 240,16 275,4 310,12 345,3 380,15 415,6 450,14 485,2 520,13 555,5 590,16 625,4 660,12 695,3 730,15 778,6 778,300 740,292 700,304 660,290 620,302 580,288 540,300 500,290 460,304 420,292 380,302 340,288 300,300 260,290 220,304 180,292 140,302 100,288 60,300 20,292 0,300"/>
  </svg>

  <div class="cta">GET STARTED</div>
  <div class="gallery-title">PHOTO GALLERY</div>

  <div class="gallery-side gallery-left" role="img" aria-label="Rendered wall project photo"></div>
  <div class="gallery-side gallery-right" role="img" aria-label="Rendered facade project photo"></div>
  <div class="gallery-main" role="img" aria-label="Freshly rendered interior wall project photo"></div>
  <svg class="arrow arrow-prev" viewBox="0 0 20 20" aria-hidden="true"><circle cx="10" cy="10" r="10" fill="#fff"/><path d="M12 5 L7 10 L12 15" stroke="#333" stroke-width="2" fill="none"/></svg>
  <svg class="arrow arrow-next" viewBox="0 0 20 20" aria-hidden="true"><circle cx="10" cy="10" r="10" fill="#fff"/><path d="M8 5 L13 10 L8 15" stroke="#333" stroke-width="2" fill="none"/></svg>

  <footer class="site-footer">
    <div class="footer-col col-links">
      <h3>QUICK LINKS</h3>
      Home<br>About Us<br>Photo Gallery<br>Contact Us
    </div>
    <div class="footer-col col-contact">
      <h3>CONTACT US</h3>
      Veltro Cement Rendering<br>Phone: (02) 5550 1234<br>Mobile: 0400 555 218<br>Email: works@veltro-render.com.au<br>Fax: (02) 5550 1235<br>Web: www.veltro-render.com.au
    </div>
    <div class="footer-col col-location">
      <h3>LOCATION</h3>
      <div class="map" role="img" aria-label="Map of the business location in Sydney"></div>
    </div>
    <div class="footer-col col-social">
      <h3>CONNECT WITH US</h3>
      <div class="social">Friendspace<i></i></div>
      <div class="social">Chirper<i></i></div>
      <div class="social">Workline<i></i></div>
    </div>
    <div class="copyright">© 2014 COMPANY NAME. ALL RIGHTS RESERVED</div>
  </footer>

</div>
</body>
</html>
```